Road Construction Company needs business cards

We would like a new business card designed for our business.

We're a road construction company based in Qld, Australia.

Can the business card please have the following information on it.

Name: Brent Halloway
Position: General Manager
Phone: 0491 257 314
Email: Brent.halloway@drovik.com.au
Address: 87 Margrove Ave, Tindale, QLD, 4016
Website: www.drovik.com.au

Visually we'd like the card to be professional and simple.

Attached is our logo.

Our website is www.drovik.com.au

Target Market(s)

Men aged 25-60

Contact Information for Business Card

As listed in project description

Font styles to use
Serif

Requirements
Must have
• Large logo on back of card

```html
<!DOCTYPE html>
<html lang="en">
<head>
<meta charset="utf-8">
<title>Drovik Business Cards</title>
<link rel="stylesheet" href="https://fonts.googleapis.com/css2?family=Poppins:wght@400;500;700;800&display=swap">
<style>
  :root {
    --backdrop: #404040;
    --card-white: #fbfbfb;
    --navy: #1753a3;
    --royal: #2161b4;
    --sky: #43a9dc;
    --ink: #3a3a3a;
    --photo-deep: #0b2a5e;
    --photo-mid: #0f4a9a;
    --photo-dark: #101a33;
  }
  * { margin: 0; padding: 0; box-sizing: border-box; }
  html, body { width: 1200px; height: 801px; overflow: hidden; }
  body {
    background: var(--backdrop);
    font-family: "Poppins", sans-serif;
    position: relative;
  }
  .card {
    position: absolute;
    top: 250px;
    width: 500px;
    height: 300px;
    overflow: hidden;
    border-radius: 2px;
    box-shadow: 0 14px 30px rgba(0,0,0,0.35);
  }
  .card-front { left: 60px; background: var(--card-white); }
  .card-back { left: 640px; }

  .front-panel { position: absolute; top: 0; right: 0; width: 500px; height: 300px; }

  .front-content { position: absolute; left: 38px; top: 48px; }
  .wordmark {
    font-weight: 800;
    font-size: 40px;
    letter-spacing: 1px;
    color: var(--navy);
    line-height: 1;
  }
  .person { margin-top: 26px; }
  .person-name {
    font-weight: 700;
    font-size: 20px;
    color: var(--navy);
    line-height: 1.1;
  }
  .person-role {
    font-weight: 400;
    font-size: 15px;
    color: var(--sky);
    margin-top: 2px;
  }
  .divider {
    width: 26px; height: 2px;
    background: var(--sky);
    margin: 12px 0 12px;
  }
  .contact { list-style: none; font-size: 11.5px; color: var(--ink); line-height: 1.5; }
  .contact li { display: flex; align-items: center; gap: 7px; }
  .contact .address { padding-left: 0; }
  .contact svg { width: 10px; height: 10px; fill: var(--navy); flex: none; }

  .photo-fill {
    position: absolute; inset: 0;
    background:
      radial-gradient(ellipse at 30% 75%, var(--photo-mid) 0%, transparent 65%),
      linear-gradient(135deg, var(--photo-deep) 0%, var(--photo-mid) 45%, var(--photo-dark) 100%);
  }
  .back-logo {
    position: absolute; left: 0; right: 0; top: 118px;
    text-align: center;
    font-weight: 800;
    font-size: 58px;
    letter-spacing: 3px;
    color: #ffffff;
    line-height: 1;
  }
</style>
</head>
<body>

  <section class="card card-front">
    <svg class="front-panel" viewBox="0 0 500 300" aria-hidden="true">
      <polygon points="330,0 500,0 500,300 420,300" fill="var(--royal)"/>
      <polygon points="380,0 500,0 500,160" fill="var(--navy)"/>
      <polygon points="395,125 500,160 420,300" fill="var(--sky)"/>
    </svg>

    <div class="front-content">
      <div class="wordmark">DROVIK</div>
      <div class="person">
        <div class="person-name">Brent Halloway</div>
        <div class="person-role">General Manager</div>
      </div>
      <div class="divider"></div>
      <ul class="contact">
        <li class="address">87 Margrove Ave,</li>
        <li class="address">Tindale, QLD, 4016</li>
        <li>
          <svg viewBox="0 0 10 10"><path d="M2 0.5l1.6 0 0.8 2.2-1.1 0.8a5.5 5.5 0 0 0 2.2 2.2l0.8-1.1 2.2 0.8 0 1.6c0 0.6-0.5 1-1 1A7.5 7.5 0 0 1 1 1.5c0-0.5 0.4-1 1-1z"/></svg>
          0491 257 314
        </li>
        <li>
          <svg viewBox="0 0 10 10"><path d="M0.5 2h9v6h-9z M0.5 2l4.5 3.5 4.5-3.5" fill="var(--navy)" stroke="#fff" stroke-width="0.6"/></svg>
          Brent.halloway@drovik.com.au
        </li>
        <li>
          <svg viewBox="0 0 10 10"><circle cx="5" cy="5" r="4.5"/><path d="M0.5 5h9M5 0.5c-2 2.5-2 6.5 0 9M5 0.5c2 2.5 2 6.5 0 9" stroke="#fff" stroke-width="0.6" fill="none"/></svg>
          www.drovik.com.au
        </li>
      </ul>
    </div>
  </section>

  <section class="card card-back">
    <div class="photo-fill" role="img" aria-label="Photo of a road roller compacting fresh asphalt, tinted deep blue"></div>
    <div class="back-logo">DROVIK</div>
  </section>

</body>
</html>
```